Outpost Lattice Advisors – Franchise Growth & Development Presentation

Outpost Lattice Advisors is an outsourced franchise sales organization (FSO) that helps franchisors grow their franchise systems without the expense and risk of hiring an internal franchise development team.

We are seeking a professional PowerPoint presentation that will be used to present our services to franchisors, franchise executives, founders, and growth-stage franchise brands.

The presentation should communicate the value of partnering with Outpost Lattice Advisors, including:

• Fractional franchise sales team versus hiring internal staff
• 30+ years of franchise industry experience
• 550+ franchise sales successes
• Immediate access to established franchise broker relationships
• Proven franchise development processes
• Franchise growth strategy and enterprise value creation
• Potential private equity and exit opportunities through franchise expansion

The presentation should feel like a modern consulting, investment, or growth strategy presentation rather than a typical sales brochure. We want strong visual storytelling, custom infographics, professional diagrams, and clean business-oriented design.

The audience includes business owners, franchise founders, franchise executives, and investors who are evaluating growth strategies for their franchise systems.

Target Market(s)

Primary Audience: Emerging franchisors Growth-stage franchise brands Franchise founders Franchise CEOs Franchise presidents Franchise development executives Secondary Audience: Private equity firms Franchise investors Strategic buyers Franchise consultants

Industry/Entity Type

Franchise Development, Private Equity / Business Expansion

Font styles to use
Other font styles liked:
• Use Montserrat for titles and Open Sans for body text.

Requirements
Must have
• Modern professional business design Consistent branding throughout Custom infographics Comparison graphics Broker network ecosystem graphic Enterprise value graphic Easy-to-read charts and visuals Editable PowerPoint format Professional iconography. www.outpostlatticeadvisors.example as reference for colors
Nice to have
• Franchise-related imagery Subtle growth-themed visuals Timeline graphics Data visualization Private equity / valuation style graphics
Should not have
• Cartoon graphics Clip art Overly busy slides Stock-template appearance Bright neon colors Handwritten fonts Excessive text on slides Juvenile or playful design elements

```html
<!DOCTYPE html>
<html lang="en">
<head>
<meta charset="utf-8">
<title>Outpost Lattice Advisors – Franchise Growth Presentation</title>
<link href="https://fonts.googleapis.com/css2?family=Montserrat:wght@300;400;500;600;700;800&family=Open+Sans:ital,wght@0,400;0,600;0,700;1,600;1,700&display=swap" rel="stylesheet">
<style>
:root{
  --navy:#1b2f57;
  --navy-deep:#14254a;
  --orange:#f7941d;
  --page:#d6d7d9;
  --panel:#eef0f3;
  --panel-line:#d3d7de;
  --ink:#1f2a44;
  --muted:#5b6478;
  --white:#ffffff;
}
*{box-sizing:border-box;margin:0;padding:0}
html,body{width:1200px;height:3692px;overflow:hidden;background:var(--page)}
body{position:relative;font-family:"Open Sans",sans-serif;color:var(--ink)}
.title-font{font-family:"Montserrat",sans-serif}
.accent{color:var(--orange)}
.icon{width:22px;height:22px;stroke:currentColor;fill:none;stroke-width:1.7;stroke-linecap:round;stroke-linejoin:round}
.badge{width:40px;height:40px;border-radius:50%;background:var(--navy);color:var(--white);display:flex;align-items:center;justify-content:center;margin:0 auto}
.badge.gray{background:#9aa1ad}

/* hero */
.hero{position:absolute;left:47px;top:47px;width:1107px;height:624px;background:var(--navy);overflow:hidden}
.hero-band{position:absolute;left:0;top:0;width:100%;height:132px;background:var(--navy)}
.hero-photo{position:absolute;left:0;top:132px;width:100%;height:492px;background:linear-gradient(100deg,#6f7b8c 0%,#a9b0ba 45%,#d9dcdf 70%,#b8bcc2 100%)}
.hero-brand{position:absolute;right:50px;top:38px;text-align:center;color:var(--white);font-family:"Montserrat",sans-serif;font-weight:800}
.hero-brand .l1{font-size:31px;letter-spacing:.5px;line-height:1}
.hero-brand .l2{font-size:15px;letter-spacing:7px;margin-top:6px}
.hero-panel{position:absolute;left:61px;top:212px;width:552px;height:350px;background:rgba(27,47,87,.72)}
.hero-copy{position:absolute;left:91px;top:245px;color:var(--white);font-family:"Montserrat",sans-serif}
.hero-copy .kicker{font-size:33px;font-weight:400;letter-spacing:.5px}
.hero-copy .big{font-size:46px;font-weight:800;line-height:1.18}
.hero-rule{width:555px;height:8px;background:var(--orange);margin:14px 0 26px -4px}
.hero-copy .sub{font-family:"Open Sans",sans-serif;font-size:25px;line-height:1.32;width:520px}

/* slides */
.slide{position:absolute;width:545px;background:var(--white);overflow:hidden}
.slide-head{height:37px;background:var(--navy);display:flex;align-items:center;justify-content:flex-end;padding-right:14px;gap:6px}
.slide-head .mark{width:8px;height:8px;background:var(--orange)}
.slide-head .name{font-family:"Montserrat",sans-serif;font-weight:800;font-size:10px;color:var(--white);letter-spacing:.5px}
.slide-title{position:absolute;left:0;width:100%;text-align:center;font-family:"Montserrat",sans-serif;font-weight:800;font-size:17px;color:var(--navy)}
.panel{position:absolute;background:var(--panel)}
.abs{position:absolute}
.label{font-family:"Montserrat",sans-serif;font-weight:600;font-size:7.5px;text-transform:uppercase;color:var(--ink);text-align:center;line-height:1.25}
.photo{position:absolute}

/* challenge */
.challenge-title{position:absolute;left:36px;top:64px;font-family:"Montserrat",sans-serif;font-weight:800;font-size:18px;line-height:1.28;color:var(--navy)}
.challenge-list{position:absolute;left:36px;top:176px;font-size:10.4px;line-height:1.45;list-style:none;width:228px}
.challenge-list li::before{content:"• "}

/* why circles */
.circle{position:absolute;border-radius:50%;display:flex;align-items:center;justify-content:center;text-align:center;font-family:"Montserrat",sans-serif;font-weight:600;font-size:8px;text-transform:uppercase;color:var(--white);line-height:1.2}
.circle.o{background:var(--orange);box-shadow:0 0 0 5px #fde2bf}
.circle.n{background:var(--navy);box-shadow:0 0 0 5px #cfd5e0}

/* cost */
.cost-box{position:absolute;background:var(--panel);border:1px solid var(--panel-line)}
.cost-box h4{font-family:"Montserrat",sans-serif;font-weight:600;font-size:8.5px;text-align:center;padding:6px 4px;border-bottom:1px solid var(--panel-line);background:#f6f7f9;text-transform:uppercase;line-height:1.25}
.cost-list{font-size:11px;line-height:1.45;padding:16px 0 0 22px}
.cost-grid{display:grid;grid-template-columns:repeat(3,1fr);row-gap:18px;padding:14px 6px}
.cost-grid div{display:flex;flex-direction:column;align-items:center;gap:5px;color:var(--navy)}
.cost-grid .icon{width:26px;height:26px}

/* process */
.steps{position:absolute;left:42px;top:152px;display:flex;gap:6px}
.step{width:60px}
.step .tab{background:var(--navy);color:var(--white);font-size:7px;text-align:center;padding:4px 0;font-family:"Montserrat",sans-serif;font-weight:600}
.step .box{height:72px;background:var(--white);border:1px solid var(--panel-line);display:flex;align-items:center;justify-content:center;color:var(--navy);margin-top:8px}
.step .box .icon{width:30px;height:30px}

/* services */
.grid4{position:absolute;display:grid;grid-template-columns:repeat(4,1fr)}
.grid4 > div{display:flex;flex-direction:column;align-items:center;gap:8px;padding:12px 4px;border-right:1px solid var(--panel-line)}
.grid4 > div:nth-child(4n){border-right:none}

/* columns */
.cols{position:absolute;display:flex}
.cols > div{flex:1;display:flex;flex-direction:column;align-items:center;gap:6px;border-right:1px solid var(--panel-line);padding:0 2px}
.cols > div:last-child{border-right:none}
.stat{font-family:"Montserrat",sans-serif;font-weight:800;font-size:15px;color:var(--orange);line-height:1}
.stat.sm{font-size:10px}

/* success */
.case{position:absolute;top:79px;width:153px;height:170px;background:var(--white);border:1px solid var(--panel-line)}
.case .img{height:123px}
.case .bar{background:var(--navy);color:var(--white);font-size:8px;padding:3px 10px;font-family:"Montserrat",sans-serif}
.case p{font-size:6.5px;line-height:1.35;color:var(--muted);padding:6px 8px;text-align:center}

/* tables */
.vt{position:absolute;border-collapse:collapse;font-size:9px;text-align:center}
.vt caption{background:var(--navy);color:var(--white);font-family:"Montserrat",sans-serif;font-weight:700;font-size:7.5px;padding:4px 0}
.vt th{font-size:6.5px;font-weight:600;text-transform:uppercase;padding:4px 3px;border-bottom:1px solid var(--panel-line);color:var(--navy)}
.vt td{padding:8px 4px;border-bottom:1px solid var(--panel-line)}
.vt td.stage{font-size:6.5px;font-weight:700;text-transform:uppercase;text-align:left}
.takeaway{position:absolute;left:29px;top:224px;width:489px;height:60px;background:var(--panel);border:1px solid var(--panel-line);display:flex;align-items:center}
.takeaway .k{display:flex;align-items:center;gap:10px;padding:0 14px;border-right:1px solid var(--panel-line);height:44px;font-family:"Montserrat",sans-serif;font-weight:800;font-size:10px;color:var(--navy);line-height:1.1}
.takeaway p{font-size:9.2px;line-height:1.4;padding:0 12px;color:var(--muted);width:300px}

/* engagement */
.eng{position:absolute;top:146px;width:90px;height:115px;display:flex;flex-direction:column;align-items:center;gap:12px;padding-top:18px}
.eng.n{background:var(--navy);color:var(--white)}
.eng.g{background:#dfe2e7;color:var(--navy)}
.eng .label{color:inherit;font-size:7px}
.eng .badge{background:var(--white);color:var(--navy)}
.eng.g .badge{background:var(--navy);color:var(--white)}

/* cta */
.cta{position:absolute;left:47px;top:3017px;width:1112px;height:482px;background:var(--navy);overflow:hidden}
.cta-map{position:absolute;left:405px;top:38px;width:700px;height:345px;background:radial-gradient(ellipse at 55% 50%,rgba(255,255,255,.22),rgba(255,255,255,.05) 65%,transparent 75%)}
.cta-copy{position:absolute;left:49px;top:38px;font-family:"Montserrat",sans-serif;font-weight:800;font-size:39px;line-height:46px;color:var(--white)}
.cta-foot{position:absolute;left:0;top:380px;width:100%;height:100px}
.social{position:absolute;left:50px;top:44px;display:flex;gap:12px}
.social span{width:24px;height:24px;border-radius:50%;background:#3a78c3}
.site{position:absolute;left:130px;top:48px;font-size:12px;color:#c9d1de}
.cta-brand{position:absolute;left:448px;top:27px;text-align:center;color:var(--white);font-family:"Montserrat",sans-serif;font-weight:800}
.cta-brand .l1{font-size:28px;line-height:1}
.cta-brand .l2{font-size:13px;letter-spacing:6px;margin-top:6px}
.cta-divider{position:absolute;left:778px;top:8px;width:1px;height:80px;background:#6f82a6}
.cta-address{position:absolute;left:796px;top:8px;font-size:15.5px;line-height:23px;color:var(--white)}

/* clients */
.clients{position:absolute;left:47px;top:3499px;width:1112px;height:144px;background:var(--white)}
.clients .cap{position:absolute;left:40px;top:8px;font-size:13px;color:var(--ink)}
.client-row{position:absolute;display:flex;align-items:center;gap:34px}
.client-row span{height:24px;background:#c7ccd4;border-radius:3px}
</style>
</head>
<body>

<svg width="0" height="0" style="position:absolute" aria-hidden="true">
  <defs>
    <symbol id="i-user" viewBox="0 0 24 24"><circle cx="12" cy="8" r="4"/><path d="M4 21c1-4 4-6 8-6s7 2 8 6"/></symbol>
    <symbol id="i-users" viewBox="0 0 24 24"><circle cx="8" cy="8" r="3"/><circle cx="16" cy="8" r="3"/><path d="M2 20c.6-3 3-5 6-5s5.4 2 6 5"/><path d="M14 15.3c.6-.2 1.3-.3 2-.3 3 0 5.4 2 6 5"/></symbol>
    <symbol id="i-chart" viewBox="0 0 24 24"><path d="M4 20h16"/><path d="M6 17v-4M10 17V9M14 17v-6M18 17V6"/><path d="M5 10l5-4 4 3 5-5"/></symbol>
    <symbol id="i-hand" viewBox="0 0 24 24"><path d="M2 11l4-4 4 2 3-2 5 0 4 4"/><path d="M6 7v6l5 5c1 1 2 1 3 0l4-4"/><path d="M10 13l3 3M12 11l3 3"/></symbol>
    <symbol id="i-doc" viewBox="0 0 24 24"><path d="M6 3h9l4 4v14H6z"/><path d="M9 10h7M9 14h7M9 18h4"/></symbol>
    <symbol id="i-gear" viewBox="0 0 24 24"><circle cx="12" cy="12" r="3.5"/><path d="M12 2v3M12 19v3M2 12h3M19 12h3M4.9 4.9l2.1 2.1M17 17l2.1 2.1M4.9 19.1L7 17M17 7l2.1-2.1"/></symbol>
    <symbol id="i-rocket" viewBox="0 0 24 24"><path d="M12 2c4 3 5 8 3 13H9C7 10 8 5 12 2z"/><circle cx="12" cy="9" r="1.8"/><path d="M9 15l-3 3 1 2 3-2M15 15l3 3-1 2-3-2M11 19v3M13 19v3"/></symbol>
    <symbol id="i-target" viewBox="0 0 24 24"><circle cx="12" cy="12" r="9"/><circle cx="12" cy="12" r="5"/><circle cx="12" cy="12" r="1.5"/></symbol>
    <symbol id="i-building" viewBox="0 0 24 24"><path d="M4 21V4h10v17M14 9h6v12M2 21h20"/><path d="M7 8h1M10 8h1M7 12h1M10 12h1M7 16h1M10 16h1M17 13h1M17 17h1"/></symbol>
    <symbol id="i-dollar" viewBox="0 0 24 24"><circle cx="12" cy="12" r="9"/><path d="M15 9c-.5-1-1.6-1.5-3-1.5-1.8 0-3 .9-3 2.2 0 3 6 1.6 6 4.6 0 1.3-1.2 2.2-3 2.2-1.5 0-2.6-.6-3-1.6M12 6v12"/></symbol>
    <symbol id="i-calendar" viewBox="0 0 24 24"><rect x="3" y="5" width="18" height="16" rx="1.5"/><path d="M3 10h18M8 3v4M16 3v4M8 14h2M13 14h2M8 17h2"/></symbol>
    <symbol id="i-trophy" viewBox="0 0 24 24"><path d="M7 4h10v5a5 5 0 0 1-10 0z"/><path d="M7 6H4c0 3 1 5 3.5 5.5M17 6h3c0 3-1 5-3.5 5.5M12 14v4M8 21h8M9 18h6"/></symbol>
    <symbol id="i-pin" viewBox="0 0 24 24"><path d="M12 22s7-7 7-12a7 7 0 0 0-14 0c0 5 7 12 7 12z"/><circle cx="12" cy="10" r="2.5"/></symbol>
    <symbol id="i-search" viewBox="0 0 24 24"><circle cx="10.5" cy="10.5" r="6.5"/><path d="M15.5 15.5L21 21"/></symbol>
    <symbol id="i-funnel" viewBox="0 0 24 24"><path d="M3 4h18l-7 8v6l-4 2v-8z"/></symbol>
    <symbol id="i-net" viewBox="0 0 24 24"><circle cx="12" cy="12" r="3"/><circle cx="4" cy="5" r="2"/><circle cx="20" cy="5" r="2"/><circle cx="4" cy="19" r="2"/><circle cx="20" cy="19" r="2"/><path d="M6 6.5l3.6 3.6M18 6.5l-3.6 3.6M6 17.5l3.6-3.6M18 17.5l-3.6-3.6"/></symbol>
    <symbol id="i-check" viewBox="0 0 24 24"><circle cx="12" cy="12" r="9"/><path d="M8 12.5l3 3 5-6"/></symbol>
    <symbol id="i-mega" viewBox="0 0 24 24"><path d="M3 10v4h4l8 5V5l-8 5z"/><path d="M18 9c1.2 1.6 1.2 4.4 0 6M7 14l1 5h3l-1-5"/></symbol>
  </defs>
</svg>

<!-- Hero -->
<section class="hero">
  <div class="hero-photo" role="img" aria-label="Photo of two business professionals reviewing work on a laptop in a bright office"></div>
  <div class="hero-band"></div>
  <div class="hero-brand"><div class="l1">OUTPOST LATTICE</div><div class="l2">ADVISORS</div></div>
  <div class="hero-panel"></div>
  <div class="hero-copy">
    <div class="kicker">OUTSOURCED</div>
    <div class="big">FRANCHISE <span class="accent">SALES</span></div>
    <div class="big">&amp; GROWTH <span class="accent">EXPERTS</span></div>
    <div class="hero-rule"></div>
    <p class="sub">Helping franchisors grow faster without the cost and risk of building an internal franchise development team.</p>
  </div>
</section>

<!-- Challenge -->
<section class="slide" style="left:47px;top:701px;height:304px">
  <div class="slide-head"><span class="mark"></span><span class="name">OUTPOST LATTICE ADVISORS</span></div>
  <h2 class="challenge-title">The Challenge<br>Facing<br><span class="accent">Emerging<br>Franchisors</span></h2>
  <ul class="challenge-list">
    <li>Limited franchise sales resources</li>
    <li>Founder wearing too many hats</li>
    <li>Inconsistent lead follow-up</li>
    <li>Difficulty recruiting franchisees</li>
    <li>Lack of broker relationships</li>
    <li>High cost of internal franchise development staff</li>
  </ul>
  <div class="photo" style="left:268px;top:44px;width:273px;height:253px;background:linear-gradient(135deg,#8a8f96,#c9c4bb 55%,#6e655c)" role="img" aria-label="Photo of an executive shaking hands with a partner across a table"></div>
</section>

<!-- Why -->
<section class="slide" style="left:614px;top:701px;height:304px">
  <div class="slide-head"><span class="mark"></span><span class="name">OUTPOST LATTICE ADVISORS</span></div>
  <h2 class="slide-title" style="top:60px">Why <span class="accent">Outpost Lattice Advisors</span></h2>
  <div class="panel" style="left:27px;top:95px;width:492px;height:193px"></div>
  <div class="circle o" style="left:124px;top:108px;width:74px;height:74px"><span><b style="font-size:10px">30+</b> YEARS<br>FRANCHISE<br>INDUSTRY<br>EXPERIENCE</span></div>
  <div class="circle o" style="left:274px;top:108px;width:74px;height:74px">IMMEDIATE<br>EXECUTION</div>
  <div class="circle o" style="left:418px;top:108px;width:74px;height:74px">DEEP BROKER<br>NETWORK<br>RELATIONSHIPS</div>
  <div class="circle n" style="left:55px;top:180px;width:74px;height:74px">FRACTIONAL<br>FRANCHISE<br>SALES TEAM</div>
  <div class="circle n" style="left:191px;top:175px;width:88px;height:88px"><span><b style="font-size:11px">550+</b><br>FRANCHISE<br>SALES<br>SUCCESSES</span></div>
  <div class="circle n" style="left:343px;top:180px;width:80px;height:80px">PROVEN<br>SYSTEMS<br>AND<br>PROCESSES</div>
</section>

<!-- Cost -->
<section class="slide" style="left:47px;top:1032px;height:281px">
  <div class="slide-head"><span class="mark"></span><span class="name">OUTPOST LATTICE ADVISORS</span></div>
  <h2 class="slide-title" style="top:62px">The Cost of Hiring vs. <span class="accent">Outsourcing</span></h2>
  <div class="cost-box" style="left:30px;top:97px;width:201px;height:174px">
    <h4>Internal Franchise<br>Development Director</h4>
    <ul class="cost-list">
      <li>Recruiting costs</li><li>Salary</li><li>Benefits</li><li>Payroll taxes</li><li>Training</li><li>Ramp-up period</li><li>Unknown performance</li>
    </ul>
  </div>
  <div class="cost-box" style="left:244px;top:97px;width:275px;height:174px">
    <h4 style="padding:12px 4px">Outpost Lattice Advisors</h4>
    <div class="cost-grid">
      <div><svg class="icon"><use href="#i-dollar"/></svg><span class="label">Fractional<br>Investment</span></div>
      <div><svg class="icon"><use href="#i-users"/></svg><span class="label">Entire Team<br>of Experts</span></div>
      <div><svg class="icon"><use href="#i-rocket"/></svg><span class="label">Immediate<br>Launch</span></div>
      <div><svg class="icon"><use href="#i-gear"/></svg><span class="label">Proven<br>Processes</span></div>
      <div><svg class="icon"><use href="#i-users"/></svg><span class="label">Existing<br>Relationships</span></div>
      <div><svg class="icon"><use href="#i-chart"/></svg><span class="label">Scalable<br>Growth</span></div>
    </div>
  </div>
</section>

<!-- Day one -->
<section class="slide" style="left:614px;top:1032px;height:281px">
  <div class="slide-head"><span class="mark"></span><span class="name">OUTPOST LATTICE ADVISORS</span></div>
  <h2 class="slide-title" style="top:62px;font-size:13px">What Takes Years to Build, <span class="accent">You Get on Day One</span></h2>
  <div class="panel" style="left:27px;top:92px;width:492px;height:178px"></div>
  <svg class="abs" style="left:196px;top:104px" width="150" height="150" viewBox="-75 -75 150 150" aria-hidden="true">
    <g stroke="#fff" stroke-width="2">
      <path d="M0-72A72 72 0 0 1 50.9-50.9L28.3-28.3A40 40 0 0 0 0-40z" fill="#1b2f57"/>
      <path d="M50.9-50.9A72 72 0 0 1 72 0L40 0A40 40 0 0 0 28.3-28.3z" fill="#b5bac3"/>
      <path d="M72 0A72 72 0 0 1 50.9 50.9L28.3 28.3A40 40 0 0 0 40 0z" fill="#f7941d"/>
      <path d="M50.9 50.9A72 72 0 0 1 0 72L0 40A40 40 0 0 0 28.3 28.3z" fill="#1b2f57"/>
      <path d="M0 72A72 72 0 0 1-50.9 50.9L-28.3 28.3A40 40 0 0 0 0 40z" fill="#b5bac3"/>
      <path d="M-50.9 50.9A72 72 0 0 1-72 0L-40 0A40 40 0 0 0-28.3 28.3z" fill="#1b2f57"/>
      <path d="M-72 0A72 72 0 0 1-50.9-50.9L-28.3-28.3A40 40 0 0 0-40 0z" fill="#f7941d"/>
      <path d="M-50.9-50.9A72 72 0 0 1 0-72L0-40A40 40 0 0 0-28.3-28.3z" fill="#1b2f57"/>
    </g>
    <circle r="36" fill="#1b2f57"/>
    <text y="-2" text-anchor="middle" fill="#fff" font-family="Montserrat" font-weight="700" font-size="8">YOU GET IT</text>
    <text y="9" text-anchor="middle" fill="#fff" font-family="Montserrat" font-weight="700" font-size="8">ON DAY ONE</text>
  </svg>
  <span class="label abs" style="left:82px;top:112px;font-size:7px">Franchise Broker<br>Relationships</span>
  <span class="label abs" style="left:355px;top:112px;font-size:7px;text-align:left">Franchise<br>Sales Expertise</span>
  <span class="label abs" style="left:78px;top:165px;font-size:7px">Lead Qualification<br>Systems</span>
  <span class="label abs" style="left:371px;top:165px;font-size:7px;text-align:left">Franchise Development<br>Processes</span>
  <span class="label abs" style="left:78px;top:216px;font-size:7px">Candidate Nurturing<br>Systems</span>
  <span class="label abs" style="left:357px;top:216px;font-size:7px;text-align:left">Industry<br>Connections</span>
  <span class="label abs" style="left:0;width:545px;top:258px;font-size:7px">CRM and Reporting Infrastructure</span>
</section>

<!-- Broker community -->
<section class="slide" style="left:47px;top:1364px;height:304px">
  <div class="slide-head"><span class="mark"></span><span class="name">OUTPOST LATTICE ADVISORS</span></div>
  <h2 class="slide-title" style="top:48px;font-size:12px">Instant Access to the <span class="accent">Franchise Broker Community</span></h2>
  <div class="panel" style="left:20px;top:70px;width:505px;height:210px;background:#f7f8fa"></div>
  <svg class="abs" style="left:20px;top:70px" width="505" height="210" aria-hidden="true">
    <g stroke="#1b2f57" stroke-width="1.2" fill="none">
      <path d="M267 76L215 22M267 76L320 22M267 76L147 88M267 76L385 88M267 76L267 163"/>
      <path d="M120 22h60M350 22h60M75 105h60M400 105h60M237 177h60"/>
    </g>
    <circle cx="267" cy="76" r="44" fill="#1b2f57" stroke="#cfd5e0" stroke-width="5"/>
    <text x="267" y="66" text-anchor="middle" fill="#fff" font-family="Montserrat" font-weight="700" font-size="10">OUTPOST</text>
    <text x="267" y="81" text-anchor="middle" fill="#f7941d" font-family="Montserrat" font-weight="800" font-size="13">LATTICE</text>
    <text x="267" y="94" text-anchor="middle" fill="#fff" font-family="Montserrat" font-weight="700" font-size="8">ADVISORS</text>
    <circle cx="215" cy="22" r="11" fill="#1b2f57"/><circle cx="320" cy="22" r="11" fill="#1b2f57"/>
    <circle cx="147" cy="88" r="11" fill="#f7941d"/><circle cx="385" cy="88" r="11" fill="#f7941d"/>
    <circle cx="267" cy="163" r="11" fill="#1b2f57"/>
    <rect x="97" y="16" width="106" height="12" rx="6" fill="#1b2f57"/>
    <text x="150" y="25" text-anchor="middle" fill="#fff" font-family="Montserrat" font-size="6">FRANCHISE CONSULTANTS</text>
    <rect x="332" y="16" width="90" height="12" rx="6" fill="#1b2f57"/>
    <text x="377" y="25" text-anchor="middle" fill="#fff" font-family="Montserrat" font-size="6">BROKER NETWORKS</text>
    <rect x="52" y="99" width="90" height="12" rx="6" fill="#f7941d"/>
    <text x="97" y="108" text-anchor="middle" fill="#fff" font-family="Montserrat" font-size="6">INDUSTRY PARTNERS</text>
    <rect x="392" y="99" width="90" height="12" rx="6" fill="#f7941d"/>
    <text x="437" y="108" text-anchor="middle" fill="#fff" font-family="Montserrat" font-size="6">REFERRAL SOURCES</text>
    <rect x="222" y="171" width="94" height="12" rx="6" fill="#1b2f57"/>
    <text x="269" y="180" text-anchor="middle" fill="#fff" font-family="Montserrat" font-size="6">FRANCHISE INFLUENCERS</text>
    <g fill="#c7ccd4">
      <rect x="50" y="38" width="38" height="10" rx="2"/><rect x="110" y="38" width="30" height="12" rx="2"/><rect x="42" y="55" width="34" height="10" rx="2"/>
      <rect x="340" y="38" width="26" height="10" rx="2"/><rect x="380" y="38" width="34" height="10" rx="2"/><rect x="395" y="56" width="40" height="10" rx="2"/>
      <rect x="42" y="130" width="28" height="10" rx="2"/><rect x="95" y="130" width="34" height="10" rx="2"/><rect x="42" y="148" width="44" height="9" rx="2"/><rect x="108" y="148" width="30" height="9" rx="2"/>
      <rect x="200" y="192" width="26" height="12" rx="2"/><rect x="234" y="192" width="24" height="12" rx="2"/><rect x="264" y="192" width="24" height="12" rx="2"/><rect x="296" y="192" width="26" height="12" rx="2"/>
    </g>
    <g fill="#1b2f57">
      <circle cx="410" cy="128" r="6"/><circle cx="432" cy="128" r="6"/><circle cx="454" cy="128" r="6"/><circle cx="476" cy="128" r="6"/><circle cx="498" cy="128" r="6"/>
    </g>
    <g font-family="Open Sans" font-size="4.5" fill="#5b6478" text-anchor="middle">
      <text x="410" y="142">Law Firms</text><text x="432" y="142">CPAs</text><text x="454" y="142">SBA Lenders</text><text x="476" y="142">Lenders</text><text x="498" y="142">Trade Assoc.</text>
    </g>
  </svg>
  <p class="abs" style="left:0;width:545px;top:284px;text-align:center;font-size:8.5px;font-weight:700;font-style:italic;color:var(--navy)">We spent over <span class="accent">20 years</span> building these relationships so <span class="accent">your brand</span> doesn't have to.</p>
</section>

<!-- Process -->
<section class="slide" style="left:614px;top:1364px;height:304px">
  <div class="slide-head"><span class="mark"></span><span class="name">OUTPOST LATTICE ADVISORS</span></div>
  <div class="panel" style="left:27px;top:63px;width:492px;height:215px"></div>
  <h2 class="slide-title" style="top:82px;line-height:1.25">Our Franchise<br><span class="accent">Development Process</span></h2>
  <div class="steps">
    <div class="step"><div class="tab">Lead</div><div class="box"><svg class="icon"><use href="#i-users"/></svg></div></div>
    <div class="step"><div class="tab">Qualification</div><div class="box"><svg class="icon"><use href="#i-doc"/></svg></div></div>
    <div class="step"><div class="tab">Education</div><div class="box"><svg class="icon"><use href="#i-building"/></svg></div></div>
    <div class="step"><div class="tab">FDD Review</div><div class="box"><svg class="icon"><use href="#i-search"/></svg></div></div>
    <div class="step"><div class="tab">Validation</div><div class="box"><svg class="icon"><use href="#i-check"/></svg></div></div>
    <div class="step"><div class="tab">Discovery Day</div><div class="box"><svg class="icon"><use href="#i-net"/></svg></div></div>
    <div class="step"><div class="tab">Franchise Award</div><div class="box"><svg class="icon"><use href="#i-trophy"/></svg></div></div>
  </div>
</section>

<!-- Services -->
<section class="slide" style="left:47px;top:1694px;height:305px">
  <div class="slide-head"><span class="mark"></span><span class="name">OUTPOST LATTICE ADVISORS</span></div>
  <h2 class="slide-title" style="top:64px">Services <span class="accent">We Provide</span></h2>
  <div class="panel" style="left:27px;top:96px;width:492px;height:189px"></div>
  <div class="grid4" style="left:27px;top:100px;width:492px">
    <div><span class="badge gray"><svg class="icon"><use href="#i-search"/></svg></span><span class="label">FDD/Operations<br>Review</span></div>
    <div><span class="badge"><svg class="icon"><use href="#i-funnel"/></svg></span><span class="label">Franchise Sales<br>Outsourcing</span></div>
    <div><span class="badge gray"><svg class="icon"><use href="#i-target"/></svg></span><span class="label">Lead<br>Qualification</span></div>
    <div><span class="badge"><svg class="icon"><use href="#i-users"/></svg></span><span class="label">Candidate<br>Nurturing</span></div>
    <div><span class="badge gray"><svg class="icon"><use href="#i-calendar"/></svg></span><span class="label">Discovery Day<br>Coordination</span></div>
    <div><span class="badge"><svg class="icon"><use href="#i-hand"/></svg></span><span class="label">Broker Recruitment/<br>Engagement</span></div>
    <div><span class="badge gray"><svg class="icon"><use href="#i-doc"/></svg></span><span class="label">CRM<br>Management</span></div>
    <div><span class="badge"><svg class="icon"><use href="#i-chart"/></svg></span><span class="label">Reporting<br>and Forecasting</span></div>
  </div>
</section>

<!-- Referral engine -->
<section class="slide" style="left:614px;top:1694px;height:305px">
  <div class="slide-head"><span class="mark"></span><span class="name">OUTPOST LATTICE ADVISORS</span></div>
  <h2 class="slide-title" style="top:57px;font-size:15px">Building a <span class="accent">Referral Engine</span> for your Brand</h2>
  <div class="photo" style="left:49px;top:92px;width:449px;height:182px;background:linear-gradient(120deg,#e9e7e2,#cfcac1 50%,#8c8478)" role="img" aria-label="Photo of a team of professionals talking in a bright modern lobby"></div>
  <div class="circle n" style="left:47px;top:85px;width:80px;height:80px;font-family:'Open Sans',sans-serif;text-transform:none;font-size:9px">Brand<br>presentations</div>
  <div class="circle o" style="left:426px;top:88px;width:80px;height:80px;font-family:'Open Sans',sans-serif;text-transform:none;font-size:9px">Broker/<br>Consultant<br>education</div>
  <div class="circle o" style="left:49px;top:198px;width:80px;height:80px;font-family:'Open Sans',sans-serif;text-transform:none;font-size:9px">Ongoing<br>Communication</div>
  <div class="circle n" style="left:429px;top:197px;width:80px;height:80px;font-family:'Open Sans',sans-serif;text-transform:none;font-size:9px">Referral<br>generation</div>
</section>

<!-- Experience -->
<section class="slide" style="left:47px;top:2025px;height:304px">
  <div class="slide-head"><span class="mark"></span><span class="name">OUTPOST LATTICE ADVISORS</span></div>
  <h2 class="slide-title" style="top:72px">Why Experience <span class="accent">Matters</span></h2>
  <div class="panel" style="left:27px;top:109px;width:492px;height:163px"></div>
  <div class="cols" style="left:27px;top:128px;width:492px;height:125px">
    <div><span class="badge"><svg class="icon"><use href="#i-trophy"/></svg></span><span class="stat">500+</span><span class="label" style="font-size:6.5px">Franchise<br>Sales Successes</span></div>
    <div><span class="badge"><svg class="icon"><use href="#i-calendar"/></svg></span><span class="stat">30+</span><span class="label" style="font-size:6.5px">Years Industry<br>Experience</span></div>
    <div><span class="badge"><svg class="icon"><use href="#i-users"/></svg></span><span class="stat sm">THOUSANDS</span><span class="label" style="font-size:6.5px">of Franchise<br>Candidates Evaluated</span></div>
    <div><span class="badge"><svg class="icon"><use href="#i-net"/></svg></span><span class="stat sm">EXTENSIVE</span><span class="label" style="font-size:6.5px">Broker Network<br>Relationships</span></div>
    <div><span class="badge"><svg class="icon"><use href="#i-building"/></svg></span><span class="stat sm">MULTI-BRAND</span><span class="label" style="font-size:6.5px">Franchise Development<br>Expertise</span></div>
  </div>
</section>

<!-- Success -->
<section class="slide" style="left:614px;top:2025px;height:304px">
  <div class="slide-head"><span class="mark"></span><span class="name">OUTPOST LATTICE ADVISORS</span></div>
  <h2 class="slide-title" style="top:50px">Success <span class="accent">Stories</span></h2>
  <div class="case" style="left:32px"><div class="img" role="img" aria-label="Photo of a businesswoman working at a laptop" style="background:linear-gradient(135deg,#c2c6cc,#8c949e)"></div><div class="bar">Case Study #1</div><p>Emerging service brand grew from 4 to 38 units within two years.</p></div>
  <div class="case" style="left:196px"><div class="img" role="img" aria-label="Photo of a presenter leading a team meeting" style="background:linear-gradient(135deg,#aab3bd,#5f6b7a)"></div><div class="bar">Case Study #2</div><p>Food concept signed 22 franchise agreements through broker referrals.</p></div>
  <div class="case" style="left:361px"><div class="img" role="img" aria-label="Photo of two executives reviewing a tablet" style="background:linear-gradient(135deg,#b9bec5,#6f7784)"></div><div class="bar">Case Study #3</div><p>Home services franchisor doubled annual royalty revenue after launch.</p></div>
</section>

<!-- Enterprise value -->
<section class="slide" style="left:47px;top:2357px;height:305px">
  <div class="slide-head"><span class="mark"></span><span class="name">OUTPOST LATTICE ADVISORS</span></div>
  <h2 class="slide-title" style="top:57px;font-size:13.5px">Building Enterprise Value <span class="accent">Through Franchise Growth</span></h2>
  <p class="abs" style="left:0;width:545px;top:78px;text-align:center;font-size:9px;color:var(--muted)">Franchise growth creates recurring royalty revenue and increases enterprise value.</p>
  <table class="vt" style="left:60px;top:109px;width:194px">
    <caption>EXAMPLE GROWTH SCENARIO</caption>
    <tr><th>Stage</th><th>Units</th><th>Annual Royalty Revenue</th></tr>
    <tr><td class="stage">Early Growth</td><td>20</td><td>$165,000</td></tr>
    <tr><td class="stage">Growth Stage</td><td>63</td><td>$1,470,000</td></tr>
  </table>
  <table class="vt" style="left:272px;top:109px;width:214px">
    <caption>ILLUSTRATIVE VALUATION RANGE</caption>
    <tr><th>Royalty Revenue</th><th>10x EBITDA</th><th>15x EBITDA</th></tr>
    <tr><td>$165,000</td><td>$1.65M</td><td>$2.48M</td></tr>
    <tr><td>$1,470,000</td><td>$14.7M</td><td>$22.05M</td></tr>
  </table>
  <div class="takeaway">
    <div class="k"><span class="badge" style="width:34px;height:34px"><svg class="icon"><use href="#i-chart"/></svg></span>KEY<br>TAKEAWAY</div>
    <p>Franchise growth is <span class="accent">not just</span> about selling franchises. It is about <span class="accent">creating recurring royalty revenue</span> that can significantly increase the value of the franchise system.</p>
    <svg class="icon" style="width:32px;height:32px;color:var(--navy)"><use href="#i-chart"/></svg>
  </div>
</section>

<!-- Exit -->
<section class="slide" style="left:614px;top:2357px;height:305px">
  <div class="slide-head"><span class="mark"></span><span class="name">OUTPOST LATTICE ADVISORS</span></div>
  <h2 class="slide-title" style="top:60px;font-size:16px">Creating Future Exit <span class="accent">Opportunities</span></h2>
  <div class="panel" style="left:27px;top:95px;width:492px;height:186px"></div>
  <p class="abs" style="left:0;width:545px;top:106px;text-align:center;font-size:9px">Potential outcomes:</p>
  <div class="cols" style="left:32px;top:130px;width:482px;height:90px">
    <div><span class="badge"><svg class="icon"><use href="#i-hand"/></svg></span><span class="label" style="font-size:6.5px">Private Equity<br>Acquisition</span><span style="width:60px;height:3px;background:var(--orange)"></span></div>
    <div><span class="badge"><svg class="icon"><use href="#i-building"/></svg></span><span class="label" style="font-size:6.5px">Strategic Buyer<br>Acquisition</span><span style="width:60px;height:3px;background:var(--orange)"></span></div>
    <div><span class="badge"><svg class="icon"><use href="#i-dollar"/></svg></span><span class="label" style="font-size:6.5px"><br>Recapitalization</span><span style="width:60px;height:3px;background:var(--orange)"></span></div>
    <div><span class="badge"><svg class="icon"><use href="#i-users"/></svg></span><span class="label" style="font-size:6.5px">Family<br>Succession</span><span style="width:60px;height:3px;background:var(--orange)"></span></div>
    <div><span class="badge"><svg class="icon"><use href="#i-chart"/></svg></span><span class="label" style="font-size:6.5px">Long-Term Cash<br>Flow Ownership</span><span style="width:60px;height:3px;background:var(--orange)"></span></div>
  </div>
  <p class="abs" style="left:0;width:545px;top:232px;text-align:center;font-size:10px;font-weight:700;font-style:italic;color:var(--navy);line-height:1.35">Every franchise sold today<br>may <span class="accent">contribute to enterprise value</span> tomorrow.</p>
</section>

<!-- Different -->
<section class="slide" style="left:47px;top:2686px;height:305px">
  <div class="slide-head"><span class="mark"></span><span class="name">OUTPOST LATTICE ADVISORS</span></div>
  <h2 class="slide-title" style="top:76px;line-height:1.25">Why Outpost Lattice<br><span class="accent">Advisors is Different</span></h2>
  <div class="panel" style="left:0;top:136px;width:545px;height:118px"></div>
  <div class="cols" style="left:10px;top:152px;width:525px;height:90px">
    <div><span class="badge"><svg class="icon"><use href="#i-user"/></svg></span><span class="label" style="font-size:6.5px">Fractional<br>Cost Model</span></div>
    <div><span class="badge"><svg class="icon"><use href="#i-rocket"/></svg></span><span class="label" style="font-size:6.5px">Immediate<br>Execution</span></div>
    <div><span class="badge"><svg class="icon"><use href="#i-users"/></svg></span><span class="label" style="font-size:6.5px"><b style="font-size:9px">550+</b><br>Franchise Sales</span></div>
    <div><span class="badge"><svg class="icon"><use href="#i-calendar"/></svg></span><span class="label" style="font-size:6.5px"><b style="font-size:9px">30+ Years'</b><br>Experience</span></div>
    <div><span class="badge"><svg class="icon"><use href="#i-net"/></svg></span><span class="label" style="font-size:6.5px">Established<br>Broker Network</span></div>
    <div><span class="badge"><svg class="icon"><use href="#i-chart"/></svg></span><span class="label" style="font-size:6.5px">Proven<br>Franchise<br>Growth Systems</span></div>
    <div><span class="badge"><svg class="icon"><use href="#i-hand"/></svg></span><span class="label" style="font-size:6.5px">Strategic<br>Growth<br>Partner</span></div>
  </div>
</section>

<!-- Engagement -->
<section class="slide" style="left:614px;top:2686px;height:305px">
  <div class="slide-head"><span class="mark"></span><span class="name">OUTPOST LATTICE ADVISORS</span></div>
  <h2 class="slide-title" style="top:97px">Engagement <span class="accent">Options</span></h2>
  <div class="eng n" style="left:27px"><span class="badge"><svg class="icon"><use href="#i-hand"/></svg></span><span class="label">Franchise<br>Sales<br>Outsourcing</span></div>
  <div class="eng g" style="left:127px"><span class="badge"><svg class="icon"><use href="#i-net"/></svg></span><span class="label">Broker<br>Network<br>Development</span></div>
  <div class="eng n" style="left:227px"><span class="badge"><svg class="icon"><use href="#i-chart"/></svg></span><span class="label">Franchise<br>Growth<br>Consulting</span></div>
  <div class="eng g" style="left:327px"><span class="badge"><svg class="icon"><use href="#i-pin"/></svg></span><span class="label">Franchise<br>Expansion<br>Strategy</span></div>
  <div class="eng n" style="left:427px"><span class="badge"><svg class="icon"><use href="#i-doc"/></svg></span><span class="label">Franchise<br>Development<br>Advisory Services</span></div>
</section>

<!-- CTA -->
<section class="cta">
  <div class="cta-map" role="img" aria-label="Dotted world map"></div>
  <h2 class="cta-copy">Let's Build Your<br>Growth Plan<br><span class="accent">Schedule a<br>Franchise<br>Growth</span><br>Strategy<br>Consultation</h2>
  <div class="cta-foot">
    <div class="social"><span></span><span></span></div>
    <span class="site">www.outpostlatticeadvisors.example</span>
    <div class="cta-brand"><div class="l1">OUTPOST LATTICE</div><div class="l2">ADVISORS</div></div>
    <div class="cta-divider"></div>
    <address class="cta-address" style="font-style:normal">418 Harbor Crest Way<br>Ste 12, Tidewater, FL 30000 USA<br>info@outpostlatticeadvisors.example</address>
  </div>
</section>

<!-- Client brands -->
<section class="clients">
  <span class="cap">Outpost Lattice Advisors</span>
  <div class="client-row" style="left:222px;top:34px">
    <span style="width:62px"></span><span style="width:62px"></span><span style="width:58px"></span><span style="width:56px"></span><span style="width:62px"></span><span style="width:64px"></span><span style="width:44px"></span><span style="width:64px"></span>
  </div>
  <div class="client-row" style="left:252px;top:90px">
    <span style="width:56px"></span><span style="width:40px"></span><span style="width:60px"></span><span style="width:60px"></span><span style="width:56px"></span><span style="width:58px"></span><span style="width:58px"></span>
  </div>
</section>

</body>
</html>
```